Dr Selwyn aesthetics - Radiance Refined

I need a logo design for a new aesthetics business in London. I am specialised in Botox, Dermal Fillers & Skin Pigmentation treatment. The slogan is Radiance Refined. I would like some of the writing on the card to be embossed. I would like a very elegant design with the following detail:

1. White and gray scale background. For the font colour try gold OR silver shades.
2. The business involves working on the face mostly. Anything that can be done with letter 'M'? Or any other logo?
3. The front of the card should have Dr Selwyn Aesthetics and the slogan 'Radiance Refined'. The back should have my full name (Dr Selwyn Tarkett), qualifications (MBBS MSC BSC), my website (www.thebrindlecliniccollective.example), telephone number & email.
4. The back should also say treatments offered: ANTI-WRINKLE INJECTIONS. DERMAL FILLERS, LIP ENHANCEMENT, HYPERHYDROSIS. SKIN PIGMENTATION

Thank you very much
Updates

Project Deadline Extended
Reason: Delays in market research response. I would be grateful for an extension please. Many thanks

Target Market(s)

Female and male aged 18 and above

Industry/Entity Type

Business

Contact Information for Business Card

Elegant design. Square corners. British standard size. Horizontal design. Should contain the slogan, contact details.

Font styles to use
Script

Colors
c9c9c9
fbed22
ffffff
f5f5f5
000000

Requirements
Must have
• All that's mentioned above
Nice to have
• A logo with the outline of a female face. Or anything that can be done with the letter M of Selwyn.
Should not have
• No colours like green / purple / orange

```html
<!DOCTYPE html>
<html lang="en">
<head>
<meta charset="utf-8">
<title>Dr Selwyn Aesthetics – Business Cards</title>
<link href="https://fonts.googleapis.com/css2?family=Questrial&display=swap" rel="stylesheet">
<style>
  :root {
    --backdrop: #e4e4e4;
    --card: #ffffff;
    --card-edge: #c9c9c9;
    --gold: #b8962a;
    --gold-deep: #9a7a1c;
    --ink-soft: #7a6a3a;
  }
  * { margin: 0; padding: 0; box-sizing: border-box; }
  html, body { width: 1200px; height: 1021px; overflow: hidden; }
  body {
    background: var(--backdrop);
    font-family: "Questrial", "Century Gothic", sans-serif;
    color: var(--gold);
    position: relative;
  }
  .card {
    position: absolute;
    width: 540px;
    height: 349px;
    background: var(--card);
    border: 1px solid var(--card-edge);
    box-shadow: 0 10px 24px rgba(0,0,0,0.12);
  }
  /* Back of card: details */
  .card-back { left: 90px; top: 80px; }
  .holder { position: absolute; top: 46px; width: 100%; text-align: center; }
  .holder-name { font-size: 25px; letter-spacing: 0.5px; color: var(--gold); }
  .holder-quals { font-size: 11px; letter-spacing: 1.5px; margin-top: 3px; color: var(--ink-soft); }
  .contact {
    position: absolute; top: 118px; width: 100%;
    text-align: center; font-size: 13px; color: var(--gold);
  }
  .contact-row { display: flex; justify-content: center; gap: 22px; align-items: center; }
  .contact-item { display: inline-flex; align-items: center; gap: 6px; }
  .contact-item svg { width: 13px; height: 13px; fill: var(--gold); }
  .contact-web { margin-top: 6px; }
  .treatments {
    position: absolute; top: 196px; left: 62px; right: 40px;
    display: grid; grid-template-columns: 1.3fr 1fr; column-gap: 20px; row-gap: 9px;
    font-size: 13px; letter-spacing: 0.3px; text-transform: uppercase; color: var(--gold-deep);
  }
  .treatment { display: flex; align-items: center; gap: 8px; }
  .treatment svg { width: 13px; height: 13px; fill: var(--gold-deep); flex: none; }

  /* Front of card: brand */
  .card-front { left: 580px; top: 470px; }
  .brand {
    position: absolute; top: 120px; width: 100%; text-align: center;
  }
  .brand-mark {
    display: inline-block; width: 18px; height: 18px; border-radius: 50%;
    background: var(--gold); vertical-align: middle; margin-right: 12px;
  }
  .brand-name { font-size: 34px; color: var(--gold); vertical-align: middle; }
  .brand-slogan {
    margin-top: 16px; font-size: 17px; letter-spacing: 5px; color: var(--gold);
  }

  /* Standalone brand lockup */
  .lockup { position: absolute; left: 60px; top: 880px; }
  .lockup .brand-mark { width: 24px; height: 24px; margin-right: 14px; }
  .lockup .brand-name { font-size: 46px; color: var(--gold-deep); }
</style>
</head>
<body>

  <section class="card card-back" aria-label="Back of business card">
    <div class="holder">
      <div class="holder-name">Dr Selwyn Tarkett</div>
      <div class="holder-quals">MBBS MSC BSC</div>
    </div>
    <div class="contact">
      <div class="contact-row">
        <span class="contact-item">
          <svg viewBox="0 0 24 24" aria-hidden="true"><path d="M6.6 10.8a15.1 15.1 0 0 0 6.6 6.6l2.2-2.2a1 1 0 0 1 1-.25 11.4 11.4 0 0 0 3.6.57 1 1 0 0 1 1 1V20a1 1 0 0 1-1 1A17 17 0 0 1 3 4a1 1 0 0 1 1-1h3.5a1 1 0 0 1 1 1c0 1.25.2 2.45.57 3.6a1 1 0 0 1-.25 1z"/></svg>
          +44 7700 900418
        </span>
        <span class="contact-item">
          <svg viewBox="0 0 24 24" aria-hidden="true"><path d="M2 5h20v14H2zm2 2v.5l8 5 8-5V7zm0 2.8V17h16V9.8l-8 5z"/></svg>
          drselwynaesthetics@example.com
        </span>
      </div>
      <div class="contact-web">www.thebrindlecliniccollective.example</div>
    </div>
    <div class="treatments">
      <div class="treatment"><svg viewBox="0 0 24 24" aria-hidden="true"><path d="M11 1h2v8.6l6.1-6.1 1.4 1.4-6.1 6.1H23v2h-8.6l6.1 6.1-1.4 1.4-6.1-6.1V23h-2v-8.6l-6.1 6.1-1.4-1.4 6.1-6.1H1v-2h8.6L3.5 4.9l1.4-1.4L11 9.6z"/></svg>Anti-wrinkle injections</div>
      <div class="treatment"><svg viewBox="0 0 24 24" aria-hidden="true"><path d="M11 1h2v8.6l6.1-6.1 1.4 1.4-6.1 6.1H23v2h-8.6l6.1 6.1-1.4 1.4-6.1-6.1V23h-2v-8.6l-6.1 6.1-1.4-1.4 6.1-6.1H1v-2h8.6L3.5 4.9l1.4-1.4L11 9.6z"/></svg>Lip enhancement</div>
      <div class="treatment"><svg viewBox="0 0 24 24" aria-hidden="true"><path d="M11 1h2v8.6l6.1-6.1 1.4 1.4-6.1 6.1H23v2h-8.6l6.1 6.1-1.4 1.4-6.1-6.1V23h-2v-8.6l-6.1 6.1-1.4-1.4 6.1-6.1H1v-2h8.6L3.5 4.9l1.4-1.4L11 9.6z"/></svg>Dermal fillers</div>
      <div class="treatment"><svg viewBox="0 0 24 24" aria-hidden="true"><path d="M11 1h2v8.6l6.1-6.1 1.4 1.4-6.1 6.1H23v2h-8.6l6.1 6.1-1.4 1.4-6.1-6.1V23h-2v-8.6l-6.1 6.1-1.4-1.4 6.1-6.1H1v-2h8.6L3.5 4.9l1.4-1.4L11 9.6z"/></svg>Hyperhydrosis</div>
      <div class="treatment"><svg viewBox="0 0 24 24" aria-hidden="true"><path d="M11 1h2v8.6l6.1-6.1 1.4 1.4-6.1 6.1H23v2h-8.6l6.1 6.1-1.4 1.4-6.1-6.1V23h-2v-8.6l-6.1 6.1-1.4-1.4 6.1-6.1H1v-2h8.6L3.5 4.9l1.4-1.4L11 9.6z"/></svg>Skin pigmentation</div>
    </div>
  </section>

  <section class="card card-front" aria-label="Front of business card">
    <div class="brand">
      <span class="brand-mark" aria-hidden="true"></span><span class="brand-name">Dr. Selwyn Aesthetics</span>
      <div class="brand-slogan">Radiance Refined</div>
    </div>
  </section>

  <div class="lockup">
    <span class="brand-mark" aria-hidden="true"></span><span class="brand-name">Dr. Selwyn Aesthetics</span>
  </div>

</body>
</html>
```